card design for engineering consultancy

engineering drafting and project management company the provides drafting services for.
Electrical, Hydraulic, Mechanical, and Civil services
The company is called Q7R Services and logo is as attached
Information on card should be.
1. Logo
2.website : Q7RServices.example
3. email : info@Q7RServices.example
4. Phone: (+61) 400512836
5. Motto: Design - Document - Develop - Deliver

this card should be basically used for business identification only

Target Market(s)

electricians plumbers air conditioning installers and civil contractors

Industry/Entity Type

engineering, drafting, electrical, plumbing, airconditioning, civil

Contact Information for Business Card

1. Logo 2.website : Q7RServices.example 3. email : info@Q7RServices.example 4. Phone: (+61) 400512836 5. Motto: Design - Document - Develop - Deliver

Font styles to use
Serif

Requirements
Must have
• logo
Nice to have
• something inovative and different that makes it stand out from being just another business card

```html
<!DOCTYPE html>
<html lang="en">
<head>
<meta charset="utf-8">
<title>Q7R Services – Business Card</title>
<link rel="stylesheet" href="https://fonts.googleapis.com/css2?family=Barlow:wght@400;500;600;700&display=swap">
<style>
  :root {
    --page: #ffffff;
    --charcoal: #504f4b;
    --red: #cf1029;
    --ink: #4a4a48;
    --card-edge: #3c3b38;
  }
  * { box-sizing: border-box; margin: 0; padding: 0; }
  html, body {
    width: 1200px; height: 848px; overflow: hidden;
    background: var(--page);
    font-family: "Barlow", Arial, sans-serif;
  }
  .canvas { position: relative; width: 1200px; height: 848px; }

  .card {
    position: absolute; top: 307px;
    width: 337px; height: 218px;
    border: 1px solid var(--card-edge);
    overflow: hidden;
  }

  /* Front */
  .card--front {
    left: 169px;
    background: var(--charcoal);
    display: flex; align-items: center; justify-content: center;
  }
  .card--front .brand-name {
    color: #ffffff;
    font-weight: 600;
    font-size: 36px;
    letter-spacing: 0.5px;
  }

  /* Back */
  .card--back { left: 672px; background: #ffffff; }
  .band { position: absolute; left: 0; right: 0; height: 15px; }
  .band--top { top: 0; background: var(--red); }
  .band--bottom { bottom: 0; background: var(--charcoal); }

  .card--back .brand-name {
    position: absolute; left: 23px; top: 48px;
    color: var(--ink);
    font-weight: 600;
    font-size: 24px;
  }

  .contact {
    position: absolute; left: 23px; top: 146px;
    list-style: none;
    font-size: 11px; line-height: 15.3px;
    color: var(--ink);
  }
  .contact .label { color: var(--red); font-weight: 500; }

  .motto {
    position: absolute; left: 218px; top: 49px;
    width: 84px;
    list-style: none;
    display: flex; flex-direction: column; align-items: center; gap: 9px;
  }
  .motto li {
    height: 23px; min-width: 62px;
    padding: 0 4px;
    border: 2.5px solid var(--ink);
    border-radius: 3px;
    display: flex; align-items: center; justify-content: center;
    color: var(--red);
    font-weight: 700; font-size: 13.5px;
  }
</style>
</head>
<body>
  <main class="canvas">
    <section class="card card--front" aria-label="Card front">
      <span class="brand-name">Q7R Services</span>
    </section>

    <section class="card card--back" aria-label="Card back">
      <div class="band band--top"></div>
      <span class="brand-name">Q7R Services</span>

      <ul class="contact">
        <li><span class="label">Website :</span> Q7RServices.example</li>
        <li><span class="label">Email :</span> info@Q7RServices.example</li>
        <li><span class="label">Phone:</span> (+61) 400 512 836</li>
      </ul>

      <ul class="motto">
        <li>Design</li>
        <li>Document</li>
        <li>Develop</li>
        <li>Deliver</li>
      </ul>

      <div class="band band--bottom"></div>
    </section>
  </main>
</body>
</html>
```